Sales Brochure

We are looking for an 8.5 x 11 folding brochure in a landscape orientation that advertises our product and service offerings. This brochure should have content on both sides.

This brochure would be left at prospect client's business, so it needs to be fresh, professional, and focused.

We have attached two 1-page inserts that we would like you to use for inspiration for the written content in the brochure. We would like the main theme of the brochure to focus on professional, repeatable, and quality IT support for business.

The brochure should have the prospective clients email or call (will provide number and email to winner) to get additional information.

Please be creative with both the content and the design.

Went on vacation/holiday

```html
<!DOCTYPE html>
<html lang="en">
<head>
<meta charset="utf-8">
<title>Norvale Sales Brochure</title>
<link href="https://fonts.googleapis.com/css2?family=Exo+2:wght@500;600;700&family=Titillium+Web:wght@400;600;700&display=swap" rel="stylesheet">
<style>
:root{
  --blue:#1a8fd6;
  --blue-deep:#1477bd;
  --blue-soft:#7db6de;
  --mist:#dce6ee;
  --mist-2:#cddbe6;
  --ink:#2b2b2b;
  --white:#ffffff;
  --stage:#bab9bf;
}
*{margin:0;padding:0;box-sizing:border-box}
html,body{width:1200px;height:580px;overflow:hidden}
body{background:var(--stage);position:relative;font-family:"Titillium Web",sans-serif;color:var(--ink)}
.page{position:absolute;top:88px;width:522px;height:404px;background:var(--white);overflow:hidden}
.page--services{left:46px}
.page--plans{left:632px}
.abs{position:absolute}
.shapes{position:absolute;left:0;top:0}
.brand{position:absolute;left:14px;top:20px;display:flex;align-items:center;gap:7px}
.brand__dot{width:26px;height:26px;border-radius:50%;background:var(--blue)}
.brand__name{font-family:"Exo 2",sans-serif;font-weight:600;font-size:30px;color:var(--blue);letter-spacing:1px;line-height:1}
.heading{font-family:"Exo 2",sans-serif;font-weight:700;color:var(--blue);letter-spacing:.6px;line-height:1.05}
.body-copy{font-size:7.4px;line-height:1.32}
.photo{position:absolute}
/* services page */
.services-title{left:17px;top:74px;font-size:19px}
.services-intro{left:17px;top:100px;width:240px}
.services-lead{left:17px;top:155px;width:200px;font-family:"Titillium Web",sans-serif;font-weight:600;font-size:9.6px;color:var(--blue);line-height:1.2}
.card{position:absolute;top:199px;width:119px;height:99px;background:var(--white);box-shadow:0 1px 4px rgba(0,0,0,.25)}
.card--tall{height:151px}
.card__tab{position:absolute;left:0;top:6px;width:44px;height:30px}
.card__title{position:absolute;left:45px;top:11px;font-family:"Exo 2",sans-serif;font-weight:700;font-size:9.4px;color:var(--blue);line-height:1;letter-spacing:.5px}
.card__text{position:absolute;left:7px;right:8px;top:40px;font-size:6.6px;line-height:1.28;text-align:justify}
.pride-banner{left:172px;top:313px;width:340px;text-align:center;font-weight:700;font-size:8.4px;line-height:1.35;color:var(--white)}
/* footer */
.footer-slogan{left:16px;top:367px;font-weight:700;font-size:11px;line-height:1.05;color:var(--white)}
.footer-contact{left:190px;top:368px;font-weight:700;font-size:8.4px;line-height:1.4;color:var(--white)}
.footer-contact span{display:flex;align-items:center;gap:4px}
.social{left:417px;top:365px;display:flex;gap:5px}
.social i{display:block;width:11px;height:11px;border-radius:50%;background:var(--white)}
.website{left:385px;top:387px;width:130px;text-align:center;font-weight:700;font-size:10.5px;color:var(--blue-deep)}
/* plans page */
.plans-tagline{left:196px;top:26px;width:320px;text-align:center;font-size:10.8px}
.plans-title{left:10px;top:84px;font-size:19px}
.plans-intro{left:11px;top:129px;width:226px;font-size:7px}
.plan-head{font-family:"Exo 2",sans-serif;font-weight:700;font-size:10px;color:var(--blue);letter-spacing:.4px}
.plan-text{font-size:6.8px;line-height:1.3;text-align:justify}
.plan--workstation{left:261px;top:69px;width:252px}
.plan--infra{left:298px;top:145px;width:215px}
.plan--data{left:337px;top:225px;width:176px}
.plan--data .plan-head,.plan--data .plan-text{color:var(--white)}
.rates{left:12px;top:338px;font-weight:700;font-size:9.6px;color:var(--blue)}
</style>
</head>
<body>

<section class="page page--services">
  <svg class="shapes" width="522" height="404" viewBox="0 0 522 404">
    <polygon points="77,6 334,6 328,18 71,18" fill="var(--blue)"/>
    <polygon points="334,6 522,6 522,18 328,18" fill="var(--mist-2)"/>
    <polygon points="0,58 522,58 522,188 290,188 280,198 0,198" fill="var(--mist)"/>
    <polygon points="176,309 522,309 522,352 146,352" fill="var(--blue)"/>
    <polygon points="166,309 176,309 146,352 136,352" fill="var(--mist-2)"/>
    <defs>
      <linearGradient id="footGradA" x1="0" x2="1">
        <stop offset="0" stop-color="#2b8ed2"/><stop offset="1" stop-color="#86b9de"/>
      </linearGradient>
    </defs>
    <rect x="0" y="360" width="522" height="44" fill="url(#footGradA)"/>
    <polygon points="0,360 200,360 180,404 0,404" fill="var(--blue-deep)" opacity=".55"/>
    <polygon points="376,384 522,384 522,404 366,404" fill="var(--white)"/>
  </svg>
  <div class="photo" role="img" aria-label="IT technician smiling at his desk in front of computer monitors"
       style="left:246px;top:22px;width:276px;height:166px;clip-path:polygon(73px 0,100% 0,100% 100%,0 100%);background:linear-gradient(120deg,#c9d3db 0%,#e7ebee 35%,#4d6589 65%,#2e4468 80%,#d7dde2 100%)"></div>

  <div class="brand"><span class="brand__dot"></span><span class="brand__name">NORVALE</span></div>
  <h1 class="abs heading services-title">NORVALE SERVICES</h1>
  <p class="abs body-copy services-intro">We provide responsive, quality IT solutions to Ridgemont, Alderbrook, Twin Pines and the surrounding areas. Our unique Core CARE™ service plans provide fast response times, and our project services provide expert IT help at an affordable price. Professionalism and reliable customer service is our standard.</p>
  <p class="abs services-lead">Here are a few ways in which we take care of your IT needs:</p>

  <article class="card card--tall" style="left:16px">
    <svg class="card__tab" viewBox="0 0 44 30"><polygon points="0,0 44,0 34,30 0,30" fill="var(--blue)"/>
      <rect x="7" y="6" width="17" height="12" rx="1" fill="none" stroke="#fff" stroke-width="1.4"/><line x1="12" y1="22" x2="19" y2="22" stroke="#fff" stroke-width="1.4"/><line x1="15.5" y1="18" x2="15.5" y2="22" stroke="#fff" stroke-width="1.4"/></svg>
    <h2 class="card__title">DESKTOP<br>SUPPORT</h2>
    <p class="card__text">Our desktop support technicians are available around the clock to respond to support calls or incidents logged in our efficient online ticketing system. Technicians respond initially by using remote support, but when the situation requires it, a technician comes on-site. Regular face-to-face IT check-ups and satisfaction surveys ensure you are pleased with the quality of the desktop support you are receiving.</p>
  </article>
  <article class="card" style="left:142px">
    <svg class="card__tab" viewBox="0 0 44 30"><polygon points="0,0 44,0 34,30 0,30" fill="var(--blue)"/>
      <rect x="7" y="5" width="8" height="19" fill="none" stroke="#fff" stroke-width="1.3"/><rect x="18" y="5" width="8" height="19" fill="none" stroke="#fff" stroke-width="1.3"/><line x1="9" y1="10" x2="13" y2="10" stroke="#fff"/><line x1="20" y1="10" x2="24" y2="10" stroke="#fff"/></svg>
    <h2 class="card__title">SYSTEMS<br>MGMNT</h2>
    <p class="card__text">We make our expertise in system and network technologies (such as email, servers, cloud, wireless, printing and remote access) work for you.</p>
  </article>
  <article class="card" style="left:266px">
    <svg class="card__tab" viewBox="0 0 44 30"><polygon points="0,0 44,0 34,30 0,30" fill="var(--blue)"/>
      <rect x="10" y="13" width="13" height="10" rx="1" fill="none" stroke="#fff" stroke-width="1.4"/><path d="M12.5 13v-3a4 4 0 0 1 8 0v3" fill="none" stroke="#fff" stroke-width="1.4"/></svg>
    <h2 class="card__title">DATA<br>PROTECTION</h2>
    <p class="card__text">We offer cost effective solutions to make sure your information is backed up securely. We ensure that backups are run properly and consistently, and monitor those backups on a daily basis.</p>
  </article>
  <article class="card" style="left:394px">
    <svg class="card__tab" viewBox="0 0 44 30"><polygon points="0,0 44,0 34,30 0,30" fill="var(--blue)"/>
      <rect x="10" y="8" width="13" height="13" fill="none" stroke="#fff" stroke-width="1.4"/><path d="M13 5v3M16.5 5v3M20 5v3M13 21v3M16.5 21v3M20 21v3M7 11h3M7 14.5h3M7 18h3M23 11h3M23 14.5h3M23 18h3" stroke="#fff" stroke-width="1.1"/></svg>
    <h2 class="card__title" style="top:12px">IT PROJECTS</h2>
    <p class="card__text">We plan, manage and implement all your technology projects. We promise to meet your stated objectives, on time and on budget.</p>
  </article>

  <p class="abs pride-banner">WE PRIDE OURSELVES IN DELIVERING SERVICES THAT INCREASE YOUR PRODUCTIVITY, HELPING YOUR BUSINESS RUN MORE EFFICIENTLY AND EFFECTIVELY. WE ARE YOUR IT++ DEPARTMENT!</p>

  <p class="abs footer-slogan">LEAVE IT TO THE<br>PROFESIONALS</p>
  <div class="abs footer-contact">
    <span><svg width="8" height="8" viewBox="0 0 10 10"><path d="M2 1l2 2-1 1.5a6 6 0 0 0 2.5 2.5L7 6l2 2-1.5 1.5C4 9 1 6 .5 2z" fill="#fff"/></svg>555-018-2240</span>
    <span><svg width="8" height="8" viewBox="0 0 10 8"><rect x=".5" y=".5" width="9" height="7" fill="none" stroke="#fff"/><path d="M.5 .5l4.5 4 4.5-4" fill="none" stroke="#fff"/></svg>sales@norvaletech.com</span>
  </div>
  <div class="abs social"><i></i><i></i><i></i><i></i></div>
  <p class="abs website">www.norvaletech.com</p>
</section>

<section class="page page--plans">
  <svg class="shapes" width="522" height="404" viewBox="0 0 522 404">
    <polygon points="158,6 420,6 414,18 152,18" fill="var(--blue)"/>
    <polygon points="420,6 522,6 522,18 414,18" fill="var(--mist-2)"/>
    <polygon points="191,56 522,56 522,127 214,127" fill="var(--mist)"/>
    <polygon points="233,137 522,137 522,213 262,213" fill="var(--mist)"/>
    <polygon points="281,220 522,220 522,357 350,357" fill="var(--blue)"/>
    <polygon points="197,61 246,61 221.5,104" fill="#fff" stroke="var(--blue)" stroke-width="1.5"/>
    <polygon points="240,142 289,142 264.5,185" fill="#fff" stroke="var(--blue)" stroke-width="1.5"/>
    <polygon points="281,223 330,223 305.5,264" fill="#fff"/>
    <rect x="214" y="65" width="14" height="14" fill="none" stroke="var(--blue)" stroke-width="1.3"/>
    <path d="M217 62v3M221 62v3M225 62v3M217 79v3M221 79v3M225 79v3M211 68h3M211 72h3M211 76h3M228 68h3M228 72h3M228 76h3" stroke="var(--blue)"/>
    <rect x="256" y="146" width="7" height="17" fill="none" stroke="var(--blue)" stroke-width="1.2"/>
    <rect x="266" y="146" width="7" height="17" fill="none" stroke="var(--blue)" stroke-width="1.2"/>
    <rect x="298" y="234" width="14" height="10" rx="1" fill="none" stroke="var(--blue)" stroke-width="1.3"/>
    <path d="M301 234v-3a4 4 0 0 1 8 0v3" fill="none" stroke="var(--blue)" stroke-width="1.3"/>
    <defs>
      <linearGradient id="footGradB" x1="0" x2="1">
        <stop offset="0" stop-color="#2b8ed2"/><stop offset="1" stop-color="#86b9de"/>
      </linearGradient>
    </defs>
    <rect x="0" y="360" width="522" height="44" fill="url(#footGradB)"/>
    <polygon points="0,360 200,360 180,404 0,404" fill="var(--blue-deep)" opacity=".55"/>
    <polygon points="376,384 522,384 522,404 366,404" fill="var(--white)"/>
  </svg>
  <div class="photo" role="img" aria-label="Businessman touching a glowing digital network of connected points"
       style="left:0;top:183px;width:245px;height:151px;background:linear-gradient(90deg,#5d87ad 0%,#9cbad3 45%,#dfe8ef 80%,#ffffff 100%)"></div>

  <div class="brand"><span class="brand__dot"></span><span class="brand__name">NORVALE</span></div>
  <p class="abs heading plans-tagline">KEEPING YOUR TECHNOLOGY SAFE AND UP-TO-DATE<br>IS NOT A ONE-TIME JOB</p>
  <h1 class="abs heading plans-title">CORE CARE™<br>SERVICE PLANS</h1>
  <p class="abs body-copy plans-intro">Our Core CARE™ service plans deliver peace of mind for all your technology data and infrastructure at an affordable price. Knowing your computers are safe and maintained saves you stress, letting you focus on what you do best. We offer plans that secure your workstation, optimize your servers and network, and keep your data safe.</p>

  <div class="abs plan--workstation">
    <h2 class="plan-head">CORE CARE™ WORKSTATION</h2>
    <p class="plan-text">You don't have time to keep up with all the latest anti-virus software or system updates, but you can't afford not to, either. Our CoreCARE™ Workstation solution delivers enterprise class anti-virus, patching, and alerting. It's maintained 24/7 by our Network Operations Center. Rest easy while we keep your computers secure.</p>
  </div>
  <div class="abs plan--infra">
    <h2 class="plan-head">CORE CARE™ INFRASTRUCTURE</h2>
    <p class="plan-text">Our CoreCARE™ Infrastructure solution ensures that your servers and other vital network devices run at peak performance. This includes being proactive about general maintenance tasks, monitoring and alerting. Because we know your IT environment, we are quickly able to handle any issues that occur, considerably speeding up recovery times.</p>
  </div>
  <div class="abs plan--data">
    <h2 class="plan-head">CORE CARE™ DATA PROTECTION</h2>
    <p class="plan-text">When was the last time you ran a full backup of your data, and then tested the data to make sure it retrieves properly? CoreCARE™ Data Protection means we monitor your backups on a daily basis. Problematic backups are brought to our attention, and we determine the cause of the problem, and make adjustments to ensure that the next backup runs successfully. In this way, we ensure that a clean, consistent copy of your data is maintained. We also perform file integrity checks to confirm that the backups are valid, and periodically conduct test file restores.</p>
  </div>
  <p class="abs rates">Rates vary based on your needs. Please contact us for pricing.</p>

  <p class="abs footer-slogan">LEAVE IT TO THE<br>PROFESIONALS</p>
  <div class="abs footer-contact">
    <span><svg width="8" height="8" viewBox="0 0 10 10"><path d="M2 1l2 2-1 1.5a6 6 0 0 0 2.5 2.5L7 6l2 2-1.5 1.5C4 9 1 6 .5 2z" fill="#fff"/></svg>555-018-2240</span>
    <span><svg width="8" height="8" viewBox="0 0 10 8"><rect x=".5" y=".5" width="9" height="7" fill="none" stroke="#fff"/><path d="M.5 .5l4.5 4 4.5-4" fill="none" stroke="#fff"/></svg>sales@norvaletech.com</span>
  </div>
  <div class="abs social"><i></i><i></i><i></i><i></i></div>
  <p class="abs website">www.norvaletech.com</p>
</section>

</body>
</html>
```